Designing a brochures for an educational counseling service provider

We would like a 4 sided design on a 11x8.5 paper, half folded. I have including a sample design we did to give you an idea of what we envision but we welcome creativity to make beautiful looking flyers. Text for the flier is included as well as our logo.
- The most important thing is capturing our audience/market. We will be handing these flies to schools, organizations and individual clients.

www.plorvaeducationalconsultants.example

Target Market(s)

We are targeting international students wanting to study in the U.S and Canada.

Industry/Entity Type

Education

Requirements
Must have
• - Clean and clear
• - Our logo should visible and well placed.
• - Could you the pictures of students, libraries and school buildings or you could use the pictures we already have.
Nice to have
• We would like this to match business cards.

```html
<!DOCTYPE html>
<html lang="en">
<head>
<meta charset="UTF-8">
<title>Educational Consultants Brochure – Inside Spread</title>
<link href="https://fonts.googleapis.com/css2?family=Open+Sans:wght@600;700&display=swap" rel="stylesheet">
<style>
  :root {
    --navy: #0e1b2e;
    --teal: #1c8a9c;
    --teal-light: #2aa7b8;
    --teal-dark: #0f5a6a;
    --slate: #3e5062;
    --paper: #f4f5f6;
    --ink: #1f2226;
    --backdrop: #d6d7d9;
  }
  * { margin: 0; padding: 0; box-sizing: border-box; }
  html, body {
    width: 1200px; height: 1200px; overflow: hidden;
    background: var(--backdrop);
    font-family: "Open Sans", Arial, sans-serif;
  }
  .spread {
    position: absolute; left: 50px; top: 175px;
    width: 1100px; height: 850px;
    display: flex;
    box-shadow: 0 20px 40px rgba(0,0,0,.18);
  }
  .page {
    position: relative; width: 550px; height: 850px;
    background: var(--paper); overflow: hidden;
  }
  .page--left { border-right: 1px solid #dcdde0; }
  .page-art { position: absolute; inset: 0; width: 100%; height: 100%; }
  .page-text {
    position: absolute; left: 48px; right: 42px;
    color: var(--ink); font-weight: 600; font-size: 11.6px;
    line-height: 1.3; text-transform: uppercase; letter-spacing: .1px;
  }
  .page--left .page-text { top: 285px; }
  .page--right .page-text { top: 122px; }
  .section-title {
    color: var(--teal); font-weight: 700; font-size: 14.5px;
    letter-spacing: .6px; margin-top: 14px; margin-bottom: 2px;
  }
  .section-title:first-child { margin-top: 0; }
  .page-text p { margin-bottom: 10px; }
  .services-tag {
    position: absolute; left: 0; top: 66px;
    background: var(--navy); color: #fff;
    font-weight: 600; font-size: 17px; letter-spacing: 1px;
    padding: 6px 36px 6px 42px; text-transform: uppercase;
  }
  .package-list { list-style: none; margin: 2px 0 8px 28px; }
  .package-list li { position: relative; padding-left: 18px; }
  .package-list li::before {
    content: ""; position: absolute; left: 0; top: 4px;
    width: 8px; height: 8px; border-radius: 50%; background: var(--navy);
  }
</style>
</head>
<body>
<div class="spread">
  <section class="page page--left">
    <svg class="page-art" viewBox="0 0 550 850" aria-hidden="true">
      <path d="M0 70 L0 250 L210 70 Z" fill="var(--teal)"/>
      <path d="M0 70 L0 130 L90 70 Z" fill="var(--teal-dark)"/>
      <path d="M0 255 L0 266 L230 70 L216 70 Z" fill="#ffffff"/>
      <path d="M380 0 L550 0 L550 95 Q480 20 380 0 Z" fill="var(--slate)"/>
      <rect x="0" y="838" width="550" height="12" fill="var(--navy)"/>
    </svg>
    <div class="page-text">
      <h2 class="section-title">Transfer Students:</h2>
      <p>Need to find a school an alternative school that is a better match for you? We work with students and families to transfer from one school to another.</p>
      <h2 class="section-title">Scholarships:</h2>
      <p>Funding the education for your children in some of the world's top schools can be very expensive as tuition and fees increase at an average of 4% every year. We work with you to determine the budget for your family, applying to scholarship available and guide you through the financial aid process.</p>
      <p>Over 70% of our clients have been awarded scholarships or financial aid, making your education goals attainable an affordable and your children education possible.</p>
      <p>Include at the bottom of last page "Our consultants are members of NAEC, the leading association for educational consultants in North America."</p>
      <h2 class="section-title">About Us:</h2>
      <p>Our mission is to make quality education accessible and affordable to the families we serve. Our services are designed with the child's future in mind. Whether one is seeking an academic or non-academic environment, it is important to us that we set our clients up for success.</p>
      <p>We are a family-centered organization and our goals are the same as those of our clients; for their child to thrive and reach their goals and dreams. With over 10 years of experience in the business, we are aware of the financial obstacles created by the ever increasing cost in education. Our expert consultants work closely with families to map out their educational budget and find the best affordable and quality educational options.</p>
    </div>
  </section>

  <section class="page page--right">
    <svg class="page-art" viewBox="0 0 550 850" aria-hidden="true">
      <rect x="0" y="0" width="550" height="8" fill="var(--navy)"/>
      <path d="M0 752 Q260 830 550 762 L550 850 L0 850 Z" fill="var(--teal)"/>
      <path d="M0 772 Q260 850 550 782 L550 850 L0 850 Z" fill="var(--teal-light)" opacity=".6"/>
      <path d="M0 792 Q260 872 550 800 L550 850 L0 850 Z" fill="var(--paper)"/>
      <path d="M0 752 Q50 790 70 850 L0 850 Z" fill="var(--navy)"/>
      <path d="M400 752 Q480 740 550 708 L550 730 Q480 752 400 752 Z" fill="var(--navy)"/>
    </svg>
    <div class="services-tag">Services:</div>
    <div class="page-text">
      <p>Finding the right school or program for your child is one of the most important decisions your family will make. The right choice will make a major impact on your child's future.</p>
      <p style="margin-bottom:2px">Our package includes:</p>
      <ul class="package-list">
        <li>Intake interview</li>
        <li>Present range of options based on needs and goals of the family</li>
        <li>Interview coaching</li>
        <li>Assistance with application and essays</li>
        <li>Updates on student progress throughout their enrollment with the school</li>
        <li>Advisement on financial documents and visa applications</li>
      </ul>
      <h2 class="section-title">Boarding Schools:</h2>
      <p>Students who want the best out of their grade school experience are likely to choose boarding schools because they are proven to better prepare students for university. North American boarding schools provide a quality dynamic experience that will facilitate personal growth in independence, leadership, and confidence as well as provide the academic curriculum necessary to prepare students for university.</p>
      <h2 class="section-title">College Admission:</h2>
      <p>As educational consultants, we specialize in college/university admissions and we understand how confusing, time-consuming, and stressful the application process can be. Our experienced counselors are here to answer your questions and guide you step by step. As parents and students may have limited access to information on schools, may not know or understand the entire process as a whole, nor where/how to begin, our experts counselors have a solutions. Clients increase the odds of admissions with our comprehensive plan of action. We believe that regardless of a student's level of involvement in extra-curricular activities or preparedness, they still possess something they can offer to the university; therefore we help them shine on their college applications.</p>
    </div>
  </section>
</div>
</body>
</html>
```